Business Card Design for Occupational Medicine Start Up Company

We need to design a professional business card. We are a healthcare company providing occupational medicine services to blue collar industries. We are professional, efficient and high quality service providers.

Target Market(s)

Blue Collar Industry: Shipbuilding, Ports, Trucking Companies; The Executives and Safety Officers for these companies

Industry/Entity Type

Healthcare

Contact Information for Business Card

Logo, Name, Title, Email, Phone

Other font styles liked:
• Please match our Brand Guide

Requirements
Must have
• Our Company Colors and Logo

```html
<!DOCTYPE html>
<html lang="en">
<head>
<meta charset="utf-8">
<title>Dockside Clinic – Business Card</title>
<link href="https://fonts.googleapis.com/css2?family=Montserrat:wght@600;700&family=Arimo:wght@400&display=swap" rel="stylesheet">
<style>
  :root {
    --navy: #232a7c;
    --navy-deep: #1d2470;
    --orange: #eba63d;
    --sky: #1e9ad6;
    --white: #ffffff;
    --paper: #f3f3f5;
    --backdrop: #dcdde1;
  }
  * { margin: 0; padding: 0; box-sizing: border-box; }
  html, body { width: 1200px; height: 800px; overflow: hidden; }
  body {
    background: var(--backdrop);
    position: relative;
    font-family: "Arimo", Arial, sans-serif;
  }
  .card {
    position: absolute;
    top: 235px;
    width: 540px;
    height: 330px;
    overflow: hidden;
    box-shadow: 0 6px 18px rgba(0,0,0,0.18);
  }
  /* Front */
  .card--front {
    left: 30px;
    background: linear-gradient(135deg, var(--navy-deep), var(--navy) 55%, #2a328a);
    display: flex;
    flex-direction: column;
    align-items: center;
    justify-content: center;
    gap: 14px;
  }
  .brand-mark {
    width: 22px; height: 22px;
    border-radius: 50%;
    background: var(--orange);
  }
  .brand-name {
    font-family: "Montserrat", Arial, sans-serif;
    font-weight: 700;
    font-size: 40px;
    letter-spacing: 1px;
    color: var(--white);
    text-align: center;
    line-height: 1.15;
  }
  /* Back */
  .card--back {
    left: 630px;
    background: linear-gradient(135deg, var(--navy-deep), var(--navy) 60%, #2a328a);
  }
  .info-band {
    position: absolute;
    left: 0; top: 0;
    width: 100%; height: 128px;
    background: linear-gradient(100deg, var(--paper), var(--white) 45%, var(--paper));
  }
  .stripe {
    position: absolute;
    left: 0;
    height: 10px;
    border-radius: 0 6px 6px 0;
  }
  .stripe--orange { top: 62px; width: 232px; background: var(--orange); }
  .stripe--navy   { top: 82px; width: 240px; background: var(--navy); }
  .stripe--sky    { top: 102px; width: 248px; background: var(--sky); }
  .person {
    position: absolute;
    left: 282px; top: 38px;
  }
  .person__name {
    font-family: "Arimo", Arial, sans-serif;
    font-size: 21px;
    color: var(--sky);
    letter-spacing: 0.5px;
  }
  .person__email {
    margin-top: 6px;
    font-size: 14px;
    color: var(--navy);
  }
  .contact-list {
    position: absolute;
    left: 48px; top: 160px;
    list-style: none;
    color: var(--white);
    font-size: 13.5px;
    line-height: 1.45;
  }
  .contact-list li {
    display: flex;
    align-items: flex-start;
    gap: 10px;
    margin-bottom: 4px;
  }
  .contact-list svg { flex: none; margin-top: 1px; }
  .back-brand {
    position: absolute;
    right: 34px; top: 205px;
    display: flex;
    align-items: center;
    gap: 10px;
  }
  .back-brand .brand-name { font-size: 22px; text-align: left; }
  .back-brand .brand-mark { width: 16px; height: 16px; }
</style>
</head>
<body>

<section class="card card--front" aria-label="Card front">
  <span class="brand-mark"></span>
  <h1 class="brand-name">DOCKSIDE<br>CLINIC</h1>
</section>

<section class="card card--back" aria-label="Card back">
  <div class="info-band">
    <span class="stripe stripe--orange"></span>
    <span class="stripe stripe--navy"></span>
    <span class="stripe stripe--sky"></span>
    <div class="person">
      <p class="person__name">FULL NAME</p>
      <p class="person__email">full.name2docksideclinic.com</p>
    </div>
  </div>

  <ul class="contact-list">
    <li>
      <svg width="18" height="18" viewBox="0 0 18 18" aria-hidden="true"><circle cx="9" cy="9" r="9" fill="var(--orange)"/><path d="M9 4a3 3 0 0 0-3 3c0 2.2 3 6 3 6s3-3.8 3-6a3 3 0 0 0-3-3z" fill="var(--navy)"/><circle cx="9" cy="7" r="1.1" fill="var(--orange)"/></svg>
      <span>123 Main Road, Suite 345<br>East North, State 12345</span>
    </li>
    <li>
      <svg width="18" height="18" viewBox="0 0 18 18" aria-hidden="true"><circle cx="9" cy="9" r="9" fill="var(--orange)"/><path d="M6 5l1.6-.4 1 2.2-1 .8a6 6 0 0 0 2.8 2.8l.8-1 2.2 1-.4 1.6c-3.5.3-7.3-3.5-7-7z" fill="var(--navy)"/></svg>
      <span>123 - 456 -7890</span>
    </li>
    <li>
      <svg width="18" height="18" viewBox="0 0 18 18" aria-hidden="true"><circle cx="9" cy="9" r="9" fill="var(--orange)"/><rect x="5" y="7" width="8" height="6" rx="1" fill="var(--navy)"/><rect x="7" y="4.5" width="4" height="3" fill="var(--navy)"/></svg>
      <span>123 - 456 7890</span>
    </li>
    <li>
      <svg width="18" height="18" viewBox="0 0 18 18" aria-hidden="true"><circle cx="9" cy="9" r="9" fill="var(--orange)"/><circle cx="9" cy="9" r="4.5" fill="none" stroke="var(--navy)" stroke-width="1.2"/><path d="M4.5 9h9M9 4.5c-2 2.5-2 6.5 0 9M9 4.5c2 2.5 2 6.5 0 9" fill="none" stroke="var(--navy)" stroke-width="1"/></svg>
      <span>docksideclinic.com</span>
    </li>
  </ul>

  <div class="back-brand">
    <span class="brand-mark"></span>
    <span class="brand-name">DOCKSIDE<br>CLINIC</span>
  </div>
</section>

</body>
</html>
```